integrative health clinic-Medical massage, acupuncture, chiropractic

we like our logo, but are open to new ideas. We need a new card design. We have added chiropractic and acupuncture that we have put under the name of the business. We are an integrative medical clinic

Target Market(s)

General public, athletes

Contact Information for Business Card

Phone 5055583927
Fax 5055583926
Hours Monday-Friday 9-6
Saturday 10-6
The 20% can be smaller on the back

Colors
3176b5
0355a3

Requirements
Must have
• Logo but am open to ideas
Nice to have
• We are an integrated medical clinic but also want to be personable. We want the card fun and inviting

```html
<!DOCTYPE html>
<html lang="en">
<head>
<meta charset="utf-8">
<title>Mesa Vista Wellness – Business Card</title>
<link rel="stylesheet" href="https://fonts.googleapis.com/css2?family=Barlow+Semi+Condensed:wght@400;500&family=EB+Garamond:ital@1&display=swap">
<style>
  :root {
    --backdrop: #a9825a;
    --card-white: #fbfbfa;
    --card-dark: #0b0d16;
    --brand-blue: #4152b3;
    --brand-blue-soft: #5a6ad0;
    --ink: #1b1c22;
    --paper-text: #f2f2f4;
  }
  * { margin: 0; padding: 0; box-sizing: border-box; }
  html, body { width: 1200px; height: 859px; overflow: hidden; }
  body {
    background: var(--backdrop);
    font-family: "Barlow Semi Condensed", "Arial Narrow", sans-serif;
    position: relative;
  }
  .card {
    position: absolute;
    top: 288px;
    width: 500px;
    height: 285px;
    overflow: hidden;
    box-shadow: 0 6px 14px rgba(0,0,0,.35);
  }
  .card--front { left: 60px; background: var(--card-white); color: var(--ink); }
  .card--back { left: 640px; background: var(--card-dark); color: var(--paper-text); }

  /* Front */
  .front__panel { position: absolute; inset: 0; }
  .front__specialty {
    position: absolute; left: 22px; top: 34px;
    font-size: 13.5px; line-height: 16px;
  }
  .contact-list { position: absolute; left: 22px; top: 104px; list-style: none; }
  .contact-list li {
    display: flex; align-items: center; gap: 7px;
    height: 19.2px; font-size: 14px;
  }
  .contact-list svg { width: 14px; height: 14px; flex: none; }
  .contact-list .accent { color: var(--brand-blue); }
  .front__address {
    position: absolute; left: 22px; top: 211px;
    font-size: 13.5px; line-height: 16px;
  }

  /* Back */
  .brand { position: absolute; left: 77px; top: 32px; width: 348px; }
  .brand__mark {
    position: absolute; left: 0; top: 6px;
    width: 44px; height: 44px; border-radius: 50%;
    background: var(--brand-blue);
  }
  .brand__name {
    position: absolute; right: 0; top: 0;
    font-size: 34px; font-weight: 500; line-height: 40px;
    color: var(--paper-text); white-space: nowrap;
  }
  .brand__tagline {
    position: absolute; right: 0; top: 41px;
    font-family: "EB Garamond", Georgia, serif; font-style: italic;
    font-size: 18px; white-space: nowrap; color: var(--paper-text);
  }
  .offer-band {
    position: absolute; left: 107px; top: 128px;
    width: 288px; height: 30px;
    background: var(--brand-blue);
    font-size: 14px; line-height: 30px; text-align: center; letter-spacing: .2px;
  }
  .book-online {
    position: absolute; left: 107px; top: 167px; width: 288px;
    font-size: 15px; text-align: center; white-space: nowrap;
  }
  .label { color: var(--brand-blue-soft); }
  .hours {
    position: absolute; right: 75px; top: 230px;
    font-size: 15px; white-space: nowrap;
  }
  .hours .divider { color: var(--brand-blue-soft); margin: 0 8px; }
  .insurance {
    position: absolute; right: 75px; top: 253px;
    font-size: 13px; white-space: nowrap;
  }
  .social-dot {
    position: absolute; left: 462px; top: 251px;
    width: 20px; height: 20px; border-radius: 50%;
    background: var(--brand-blue);
  }
</style>
</head>
<body>

<section class="card card--front" aria-label="Card front">
  <svg class="front__panel" viewBox="0 0 500 285" width="500" height="285" aria-hidden="true">
    <path d="M500 0 H340 C270 40 250 150 295 215 C325 260 360 280 400 285 H500 Z" fill="var(--card-dark)"/>
  </svg>

  <p class="front__specialty">Specializing in Medical, Sports<br>Massage and Manual Therapies</p>

  <ul class="contact-list">
    <li>
      <svg viewBox="0 0 16 16" aria-hidden="true"><circle cx="8" cy="8" r="6.8" fill="none" stroke="var(--brand-blue)" stroke-width="1.3"/><path d="M5.6 4.8l1.3-.3.7 1.6-.8.7c.4.9 1 1.5 1.9 1.9l.7-.8 1.6.7-.3 1.3c-2.6.2-5.2-2.4-5.1-5.1z" fill="var(--brand-blue)"/></svg>
      505 558 3927
    </li>
    <li>
      <svg viewBox="0 0 16 16" aria-hidden="true"><rect x="4" y="1.5" width="8" height="4" fill="var(--brand-blue)"/><rect x="1" y="5.5" width="14" height="6" rx="1.2" fill="var(--brand-blue)"/><rect x="4" y="10" width="8" height="4.5" fill="#fff" stroke="var(--brand-blue)" stroke-width="1.2"/></svg>
      505 558 3926
    </li>
    <li>
      <svg viewBox="0 0 16 16" aria-hidden="true"><rect x="1.2" y="3.2" width="13.6" height="9.6" fill="none" stroke="var(--brand-blue)" stroke-width="1.3"/><path d="M1.5 3.5 8 9l6.5-5.5M1.5 12.5l5-4.5M14.5 12.5l-5-4.5" fill="none" stroke="var(--brand-blue)" stroke-width="1.1"/></svg>
      info@mesavistawellness.com
    </li>
    <li>
      <svg viewBox="0 0 16 16" aria-hidden="true"><circle cx="8" cy="8" r="6.8" fill="none" stroke="var(--brand-blue)" stroke-width="1.3"/><ellipse cx="8" cy="8" rx="3" ry="6.8" fill="none" stroke="var(--brand-blue)" stroke-width="1.1"/><path d="M1.3 8h13.4M2.3 4.6h11.4M2.3 11.4h11.4" stroke="var(--brand-blue)" stroke-width="1.1"/></svg>
      <span>www.<span class="accent">mesavistawellness</span>.com</span>
    </li>
  </ul>

  <p class="front__address">1487 Cerrillos Rd, B4. Santa Fe<br>NM 87505</p>
</section>

<section class="card card--back" aria-label="Card back">
  <div class="brand">
    <span class="brand__mark" aria-hidden="true"></span>
    <span class="brand__name">Mesa Vista Wellness</span>
    <span class="brand__tagline">Sports Therapy and Wellness Center</span>
  </div>

  <div class="offer-band">20% OFF FIRST VISIT</div>

  <p class="book-online"><span class="label">BOOK ONLINE:</span> www.mesavistawellness.com</p>

  <p class="hours"><span class="label">HOURS:</span> Monday-Friday 9am-6pm<span class="divider">|</span>Saturday 10am-6pm</p>
  <p class="insurance">We accept some insurances, Worker,s Comp and Personal Injury</p>

  <span class="social-dot" aria-hidden="true"></span>
</section>

</body>
</html>
```